Brightfold Partners Website

Brightfold Partners (BP) provide Analytics & Enterprise Performance Management (EPM) advisory & consultancy services. We are passionate about data and making a difference for our clients by working in partnership with them, helping them on their journey to becoming an Brightfold Partner. We deliver insights which give our clients a competitive edge and a much deeper understanding of their organisation.

We need a website which shows who we are, what we do and how we do it.

www.brightfold-partners.example is our very basic website at the moment. We want to completely revamp it with a corporate look

```html
<!DOCTYPE html>
<html lang="en">
<head>
<meta charset="utf-8">
<title>Brightfold Partners — Data Analytics &amp; EPM Consulting</title>
<link rel="stylesheet" href="https://fonts.googleapis.com/css2?family=Montserrat:wght@500;600;700;800&family=Roboto:wght@400;500;700&display=swap">
<style>
  :root {
    --brand: #2b5572;
    --brand-dark: #1f4560;
    --brand-deep: #1a3a52;
    --ink: #2a2a2a;
    --muted: #555;
    --paper: #ffffff;
    --mist: #f0f0f0;
    --frame: #c5d3dd;
    --white: #ffffff;
  }
  * { box-sizing: border-box; margin: 0; padding: 0; }
  html, body { width: 1200px; height: 3715px; overflow: hidden; background: var(--paper); }
  body { position: relative; font-family: "Roboto", sans-serif; color: var(--ink); }
  .abs { position: absolute; }
  .heading { font-family: "Montserrat", sans-serif; font-weight: 800; color: var(--brand); letter-spacing: 1px; }

  /* Header */
  .site-header { position: absolute; left: 0; top: 0; width: 1200px; height: 137px; background: var(--paper); }
  .brand { position: absolute; display: flex; align-items: center; gap: 16px; }
  .brand-dot { width: 70px; height: 70px; border-radius: 50%; background: var(--brand); flex: none; }
  .brand-name { font-family: "Montserrat", sans-serif; font-weight: 700; font-size: 27px; line-height: 31px; color: var(--brand); letter-spacing: 1px; }
  .phone { position: absolute; left: 952px; top: 22px; display: flex; align-items: center; gap: 12px; font-family: "Roboto", sans-serif; font-weight: 500; font-size: 20px; color: var(--ink); }
  .phone-dot { width: 30px; height: 30px; border-radius: 50%; background: var(--brand); }
  .main-nav a { position: absolute; top: 76px; font-family: "Montserrat", sans-serif; font-weight: 600; font-size: 19px; color: var(--brand); text-decoration: none; }

  /* Hero */
  .hero { position: absolute; left: 0; top: 137px; width: 1200px; height: 642px;
    background: radial-gradient(ellipse at 60% 45%, #6a6660 0%, #3d3a37 50%, #1e1d1c 100%); }
  .hero-title { position: absolute; left: 0; width: 1200px; top: 222px; text-align: center; font-family: "Montserrat", sans-serif; font-weight: 700; font-size: 48px; color: var(--white); letter-spacing: 1px; }
  .hero-sub { position: absolute; left: 0; width: 1200px; top: 291px; text-align: center; font-family: "Roboto", sans-serif; font-weight: 700; font-size: 22px; color: var(--white); }
  .btn { position: absolute; display: flex; align-items: center; gap: 12px; border-radius: 26px; font-family: "Montserrat", sans-serif; font-weight: 700; color: var(--white); text-decoration: none; }
  .btn-dot { width: 34px; height: 34px; border-radius: 50%; background: var(--white); flex: none; }
  .btn-hero { left: 499px; top: 349px; width: 202px; height: 51px; padding-left: 10px; border: 2px solid var(--white); background: var(--brand); font-size: 19px; }

  /* Who we are */
  .who-frame { position: absolute; left: 101px; top: 924px; width: 249px; height: 237px; border: 9px solid var(--frame); border-radius: 6px; }
  .dot-grid { position: absolute; left: 101px; top: 1263px; width: 187px; height: 186px;
    background-image: radial-gradient(circle, #b8b8b8 1.4px, transparent 1.6px); background-size: 12px 12px; }
  .photo { position: absolute; }
  .photo-main { left: 137px; top: 953px; width: 420px; height: 446px; background: linear-gradient(135deg, #e9c9c6 0%, #bcb6b0 40%, #4a4c55 100%); }
  .photo-inset { left: 353px; top: 1226px; width: 237px; height: 223px; border: 3px solid var(--brand); background: linear-gradient(160deg, #eeeeee 0%, #cfc7bd 50%, #6b6560 100%); }
  .who-title { position: absolute; left: 591px; top: 925px; font-size: 58px; }
  .who-text { position: absolute; left: 663px; width: 425px; font-size: 19px; line-height: 29px; color: var(--ink); }
  .btn-more { left: 663px; top: 1360px; width: 198px; height: 49px; padding-left: 8px; background: var(--brand); font-size: 19px; }
  .who-watermark { position: absolute; left: 1128px; top: 1082px; writing-mode: vertical-rl; font-family: "Montserrat", sans-serif; font-weight: 800; font-size: 40px; color: #f1f1f1; letter-spacing: 2px; }

  /* What we do */
  .services { position: absolute; left: 0; top: 1575px; width: 1200px; height: 783px; background: var(--mist); }
  .services-net { position: absolute; left: 0; top: 2180px; width: 1200px; height: 178px; background: linear-gradient(180deg, rgba(240,240,240,0) 0%, #e6e6e6 100%); }
  .services-title { position: absolute; left: 0; width: 1200px; top: 1650px; text-align: center; font-size: 58px; }
  .service-photo { position: absolute; top: 1755px; width: 314px; height: 346px; }
  .service-card { position: absolute; top: 2031px; width: 289px; height: 200px; background: var(--paper); border-bottom: 4px solid var(--brand); padding: 44px 26px 0 26px; box-shadow: 0 2px 6px rgba(0,0,0,.08); }
  .service-card.is-active { background: var(--brand); }
  .service-card h3 { font-family: "Montserrat", sans-serif; font-weight: 700; font-size: 19px; color: var(--brand); margin-bottom: 12px; }
  .service-card p { font-size: 13px; line-height: 19px; color: var(--ink); }
  .service-card.is-active h3, .service-card.is-active p { color: var(--white); }

  /* How we do it */
  .how-title { position: absolute; left: 0; width: 1200px; top: 2440px; text-align: center; font-size: 58px; }
  .step { position: absolute; width: 210px; }
  .step h4 { font-family: "Montserrat", sans-serif; font-weight: 700; font-size: 17px; color: var(--brand); margin-bottom: 10px; }
  .step p { font-size: 12px; line-height: 17px; color: var(--ink); }
  .step-left { text-align: right; }

  /* Footer */
  .site-footer { position: absolute; left: 0; top: 3000px; width: 1200px; height: 715px; background: linear-gradient(180deg, var(--brand) 0%, var(--brand-dark) 100%); border-top: 4px solid #9aa9b4; }
  .footer-base { position: absolute; left: 0; top: 3488px; width: 1200px; height: 227px; background: var(--brand-deep); }
  .footer-brand .brand-dot { background: var(--white); }
  .footer-brand .brand-name { color: var(--white); }
  .contact-item { position: absolute; left: 101px; display: flex; gap: 20px; color: var(--white); }
  .contact-icon { width: 40px; height: 40px; border-radius: 50%; border: 2px solid var(--white); display: flex; align-items: center; justify-content: center; flex: none; }
  .contact-label { font-family: "Montserrat", sans-serif; font-weight: 500; font-size: 19px; line-height: 22px; }
  .contact-value { font-size: 13px; line-height: 22px; }
  .contact-title { position: absolute; left: 544px; top: 3095px; font-family: "Montserrat", sans-serif; font-weight: 700; font-size: 39px; color: var(--white); }
  .field { position: absolute; border: 1.5px solid #c8d3db; padding: 10px 14px; font-size: 14px; color: var(--white); }
  .btn-submit { position: absolute; left: 544px; top: 3405px; width: 109px; height: 36px; border-radius: 18px; background: var(--white); color: var(--brand); font-family: "Montserrat", sans-serif; font-weight: 700; font-size: 16px; display: flex; align-items: center; justify-content: center; }
  .footer-nav a { position: absolute; top: 3549px; font-family: "Montserrat", sans-serif; font-weight: 500; font-size: 19px; color: var(--white); text-decoration: none; }
  .copyright { position: absolute; left: 0; width: 1200px; top: 3593px; text-align: center; font-family: "Montserrat", sans-serif; font-size: 14px; color: var(--white); }
  .social { position: absolute; top: 3630px; width: 50px; height: 50px; border-radius: 50%; border: 2px solid var(--white); display: flex; align-items: center; justify-content: center; }
  .social-fill { width: 34px; height: 34px; border-radius: 50%; background: var(--white); }
</style>
</head>
<body>

<header class="site-header">
  <div class="brand" style="left:101px; top:28px;">
    <span class="brand-dot"></span>
    <span class="brand-name">BRIGHTFOLD<br>PARTNERS</span>
  </div>
  <div class="phone"><span class="phone-dot"></span>01 555 0142</div>
  <nav class="main-nav">
    <a href="#" style="left:513px;">HOME</a>
    <a href="#" style="left:627px;">ABOUT US</a>
    <a href="#" style="left:783px;">OUR SERVICES</a>
    <a href="#" style="left:982px;">CONTACT US</a>
  </nav>
</header>

<section class="hero" role="img" aria-label="Business team reviewing financial charts around a meeting table">
  <h1 class="hero-title">BRIGHTFOLD PARTNERS</h1>
  <p class="hero-sub">DATA ANALYTICS &amp; EPM CONSULTING SERVICES</p>
  <a class="btn btn-hero" href="#"><span class="btn-dot"></span>CONTACT US</a>
</section>

<section class="who">
  <div class="who-frame"></div>
  <div class="dot-grid"></div>
  <div class="photo photo-main" role="img" aria-label="Two businessmen in discussion at a desk"></div>
  <div class="photo photo-inset" role="img" aria-label="Colleagues shaking hands across a meeting table"></div>
  <h2 class="heading who-title">WHO WE ARE</h2>
  <p class="who-text" style="top:1022px;">Brightfold Partners is an exciting start-up in the Data Analytics and EPM space.&nbsp; Founded in 2019, BP specialise in the implementation and support of BI, EPM and Data Analytics business solutions, both in the Cloud and on-premise.</p>
  <p class="who-text" style="top:1189px;">Lorem ipsum dolor sit amet, consectetur adipi scing elit, sed do eiusmod tempor incididunt ut labore et dolore magna aliqua. Quis ipsum suspe ndisse ultrices gravida. Risus commodo viverra maecenas accumsan lacus vel facilisis.</p>
  <a class="btn btn-more" href="#"><span class="btn-dot"></span>READ MORE</a>
  <div class="who-watermark">WHO WE ARE</div>
</section>

<section class="services">
</section>
<div class="services-net"></div>
<h2 class="heading services-title">WHAT WE DO</h2>
<div class="service-photo" style="left:100px; background:linear-gradient(160deg,#d9dadb 0%,#b4b6b8 60%,#8c8f92 100%);" role="img" aria-label="Hands signing documents at a desk"></div>
<div class="service-photo" style="left:443px; background:linear-gradient(160deg,#4f7890 0%,#2d566f 60%,#1d3c52 100%);" role="img" aria-label="Person at a laptop with overlaid process icons"></div>
<div class="service-photo" style="left:786px; background:linear-gradient(160deg,#cfd6da 0%,#5aa3c8 50%,#2d4a5e 100%);" role="img" aria-label="Laptop displaying analytics dashboard"></div>
<article class="service-card" style="left:112px;">
  <h3>ADVISE &amp; ARCHITECT</h3>
  <p>Helping our customers understand the art of the possible and safeguarding their investments by overseeing implementations.</p>
</article>
<article class="service-card is-active" style="left:456px;">
  <h3>DESIGN &amp; IMPLEMENT</h3>
  <p style="font-size:12px;">Working with the project management team, through each stage of the project, with clearly defined deliverables and well exercised plans to deliver them.</p>
</article>
<article class="service-card" style="left:799px;">
  <h3>OPTIMISE &amp; MANAGE</h3>
  <p style="font-size:12px;">Our Managed Services delivers proactive, on-demand support for EPM and Data Analytics environments.</p>
</article>

<section class="how">
  <h2 class="heading how-title">HOW WE DO IT</h2>
  <svg class="abs" style="left:0; top:2358px;" width="1200" height="642" viewBox="0 2358 1200 642">
    <circle cx="600" cy="2737" r="163" fill="none" stroke="var(--brand)" stroke-width="4"/>
    <circle cx="472" cy="2644" r="9" fill="var(--brand)"/>
    <circle cx="728" cy="2644" r="9" fill="var(--brand)"/>
    <circle cx="453" cy="2795" r="9" fill="var(--brand)"/>
    <circle cx="746" cy="2795" r="9" fill="var(--brand)"/>
    <g fill="var(--brand)">
      <circle cx="398" cy="2629" r="41"/>
      <circle cx="382" cy="2794" r="41"/>
      <circle cx="806" cy="2632" r="41"/>
      <circle cx="812" cy="2807" r="41"/>
    </g>
    <g fill="none" stroke="#fff" stroke-width="2.5" stroke-linecap="round">
      <circle cx="390" cy="2626" r="7"/><path d="M378 2648 q12-14 24 0"/><rect x="402" y="2606" width="18" height="12" rx="2"/>
      <circle cx="382" cy="2788" r="8"/><path d="M368 2772 l-8-8 M396 2772 l8-8 M382 2796 l-8 18 M382 2796 l8 18"/>
      <circle cx="806" cy="2632" r="16"/><path d="M798 2632 l6 6 l10-12"/>
      <circle cx="804" cy="2805" r="7"/><path d="M792 2827 q12-14 24 0"/><rect x="816" y="2784" width="18" height="12" rx="2"/>
    </g>
  </svg>
  <div class="step step-left" style="left:116px; top:2576px;">
    <h4>Finibus Bonorum</h4>
    <p>Lorem ipsum dolor sit amet, consec tetur adipiscing elit, sed do eiusmod tempor incididunt ut labore et dolore magna aliquaenim ad dolo</p>
  </div>
  <div class="step step-left" style="left:116px; top:2750px;">
    <h4>Finibus Bonorum</h4>
    <p>Lorem ipsum dolor sit amet, consec tetur adipiscing elit, sed do eiusmod tempor incididunt ut labore et dolore magna aliquaenim ad dolo</p>
  </div>
  <div class="step" style="left:877px; top:2589px;">
    <h4>Finibus Bonorum</h4>
    <p>Lorem ipsum dolor sit amet, consec tetur adipiscing elit, sed do eiusmod tempor incididunt ut labore et dolore magna aliquaenim ad dolo</p>
  </div>
  <div class="step" style="left:877px; top:2758px;">
    <h4>Finibus Bonorum</h4>
    <p>Lorem ipsum dolor sit amet, consec tetur adipiscing elit, sed do eiusmod tempor incididunt ut labore et dolore magna aliquaenim ad dolo</p>
  </div>
</section>

<footer class="site-footer"></footer>
<div class="footer-base"></div>
<div class="brand footer-brand" style="left:101px; top:3108px;">
  <span class="brand-dot" style="width:80px;height:80px;"></span>
  <span class="brand-name" style="font-size:28px;">BRIGHTFOLD<br>PARTNERS</span>
</div>
<div class="contact-item" style="top:3230px;">
  <span class="contact-icon"><svg width="20" height="22" viewBox="0 0 20 22"><path d="M10 21 C4 13 2 10 2 8 a8 8 0 0 1 16 0 c0 2-2 5-8 13z" fill="none" stroke="#fff" stroke-width="2"/><circle cx="10" cy="8" r="3" fill="#fff"/></svg></span>
  <div><div class="contact-label">ADDRESS:</div><div class="contact-value">12 Harbour Lane, Millbrook,<br>Dublin 9, D09 XR21</div></div>
</div>
<div class="contact-item" style="top:3317px;">
  <span class="contact-icon"><svg width="20" height="20" viewBox="0 0 20 20"><path d="M4 2 l4 0 l1 5 l-3 2 q2 4 5 5 l2-3 l5 1 l0 4 q-1 2-3 2 Q4 17 2 4 q0-2 2-2z" fill="#fff"/></svg></span>
  <div><div class="contact-label">PHONE:</div><div class="contact-value">01 555 0142</div></div>
</div>
<div class="contact-item" style="top:3380px;">
  <span class="contact-icon"><svg width="22" height="16" viewBox="0 0 22 16"><rect x="1" y="1" width="20" height="14" fill="none" stroke="#fff" stroke-width="2"/><path d="M1 1 l10 8 l10-8" fill="none" stroke="#fff" stroke-width="2"/></svg></span>
  <div><div class="contact-label">EMAIL:</div><div class="contact-value">info@brightfold-partners.example</div></div>
</div>

<h2 class="contact-title">CONTACT US</h2>
<div class="field" style="left:544px; top:3163px; width:254px; height:40px;">First Name:</div>
<div class="field" style="left:813px; top:3163px; width:254px; height:40px;">Last Name:</div>
<div class="field" style="left:544px; top:3219px; width:254px; height:41px;">Email Address:</div>
<div class="field" style="left:813px; top:3219px; width:254px; height:41px;">Phone Number:</div>
<div class="field" style="left:544px; top:3277px; width:523px; height:105px;">Message:</div>
<div class="btn-submit">SUBMIT</div>

<nav class="footer-nav">
  <a href="#" style="left:312px;">HOME</a>
  <a href="#" style="left:421px;">ABOUT US</a>
  <a href="#" style="left:571px;">OUR SERVICES</a>
  <a href="#" style="left:763px;">CONTACT US</a>
</nav>
<p class="copyright">Copyright © 2022.BRIGHTFOLD PARTNERS</p>
<a class="social" style="left:510px;" href="#" aria-label="Email"><svg width="26" height="18" viewBox="0 0 26 18"><rect x="1" y="1" width="24" height="16" fill="#fff"/><path d="M1 1 l12 9 l12-9" fill="none" stroke="var(--brand)" stroke-width="2"/></svg></a>
<a class="social" style="left:575px;" href="#" aria-label="Social profile"><span class="social-fill"></span></a>
<a class="social" style="left:637px;" href="#" aria-label="Social profile"><span class="social-fill"></span></a>

</body>
</html>
```